Label and logo design for organic food range

We are looking to a new label and logo design for a brand new range of organic foods. We have a conventional product range branded as veldhoeve and we are launching a new line of organic products under the brandname "naturavel"

For reference I attached the logo of veldhoeve which we like it very much, but we think that we would need an upgraded, more fresh logo design for our new brand.

I also attached a label for a veldhoeve product, we use only one label on the products (packed in transparent bags), so the label must contains a lot of text and informations as you can see on the veldhoeve label. (mostly it should contain all the text on the label attached)

Target Market(s)

organic products, bio products, health stores

Industry/Entity Type

Health Product

Logo Text

the healthy choice

Font styles to use
Sans Serif
Other font styles liked:
• CabinSketch, Bebas Neue, Chalkboard,

Colors
9bcb3b
00a990
fbed22
f78f20
faa54b
fac994
f37122
f68d4d
ec1f27

Requirements
Nice to have
• As a reference, I attached 3 labels (same brand I like very much, 1,2,3.jpg). Default label size is 64mm x 100mm ( + 2.5mm bleed). I also attached the texts on the label (label-text.docx)

```html
<!DOCTYPE html>
<html lang="ro">
<head>
<meta charset="utf-8">
<title>naturavel – Raw Almond label</title>
<link rel="stylesheet" href="https://fonts.googleapis.com/css2?family=Baloo+2:wght@700&family=Arimo:wght@400;700&display=swap">
<style>
  :root {
    --canvas: #f4f4f2;
    --label-red: #ef5a3a;
    --label-white: #ffffff;
    --ink: #3a3a3a;
    --rule: #222222;
    --nut-dark: #8a5a34;
    --nut-light: #d9a275;
  }
  * { box-sizing: border-box; margin: 0; padding: 0; }
  html, body { width: 800px; height: 1200px; overflow: hidden; }
  body { background: var(--canvas); position: relative; font-family: "Arimo", Arial, sans-serif; }

  .label {
    position: absolute; left: 60px; top: 108px;
    width: 680px; height: 984px;
    background: var(--label-red);
    overflow: hidden;
  }
  .label__swirl { position: absolute; inset: 0; }

  .brand {
    position: absolute; left: 64px; top: 110px;
    display: flex; align-items: center; gap: 14px;
    font-family: "Baloo 2", sans-serif; font-weight: 700;
    font-size: 64px; line-height: 1; color: var(--label-white);
  }
  .brand__dot { width: 22px; height: 22px; border-radius: 50%; background: var(--label-white); }

  .product-name {
    position: absolute; left: 70px; top: 400px;
    font-family: "Baloo 2", sans-serif; font-weight: 700;
    color: var(--label-white); line-height: 0.9;
    transform: rotate(-6deg); transform-origin: left top;
  }
  .product-name__raw { display: block; font-size: 58px; margin-left: 16px; }
  .product-name__kind { display: block; font-size: 74px; }

  .info {
    position: absolute; left: 357px; top: 180px; width: 300px;
    font-size: 15px; line-height: 18.5px; color: var(--ink); text-align: justify;
  }
  .info p + p { margin-top: 10px; }

  .product-photo {
    position: absolute; left: 48px; top: 620px; width: 290px; height: 364px;
    border-radius: 0 150px 0 0;
    background: radial-gradient(circle at 45% 55%, var(--nut-light), var(--nut-dark) 75%);
  }

  .nutrition {
    position: absolute; left: 357px; top: 613px; width: 212px;
    border-collapse: collapse; background: var(--label-white);
    font-size: 13.5px; color: var(--ink);
  }
  .nutrition th, .nutrition td { border: 1.5px solid var(--rule); padding: 3px 5px; height: 25px; }
  .nutrition th { font-weight: 400; text-align: left; font-size: 12.5px; }
  .nutrition td:last-child { text-align: right; width: 58px; }
  .nutrition tr.nutrition__gap td { height: 10px; padding: 0; }

  .net-weight {
    position: absolute; left: 596px; top: 672px;
    font-size: 30px; font-weight: 700; color: var(--ink);
    transform: rotate(-90deg); transform-origin: center;
  }
  .distributor {
    position: absolute; left: 580px; top: 860px; width: 240px;
    font-size: 13px; line-height: 15px; color: var(--ink);
    transform: rotate(-90deg); transform-origin: left top;
    translate: 0 120px;
  }
</style>
</head>
<body>
  <article class="label">
    <svg class="label__swirl" viewBox="0 0 680 984" aria-hidden="true">
      <path fill="#ffffff" d="M0 650 C90 600 230 630 320 580 C400 535 410 400 470 340 C530 280 640 310 640 410 C640 490 570 540 530 600 C480 670 470 800 430 880 C410 930 385 965 365 984 L0 984 Z"/>
      <path fill="#ef5a3a" d="M490 390 C530 370 585 395 585 440 C585 490 540 520 515 560 C490 520 460 440 490 390 Z"/>
    </svg>

    <div class="brand"><span class="brand__name">naturavel</span><span class="brand__dot"></span></div>

    <h1 class="product-name"><span class="product-name__raw">RAW</span><span class="product-name__kind">ALMOND</span></h1>

    <div class="info">
      <p>Mod de utilizare: Se pot consuma ca atare sau prăjite în diverse combinații cu legume, sosuri, cereale și deserturi. A se consuma, de preferință, înainte de data marcată pe ambalaj.</p>
      <p>Ingrediente: sâmburi de Migdale crude. Depozitare: A se păstra la loc uscat și răcoros. Atenționare: produsul conține substanțe cu potențial alergen: migdale. Țara de origine: SUA.</p>
      <p>Produs într-o unitate care ambalează și procesează făină din cereale, muștar, soia, nuci, alune, semințe de susan.</p>
    </div>

    <div class="product-photo" role="img" aria-label="Photograph of raw almonds"></div>

    <table class="nutrition">
      <tr><th colspan="2">VALORI NUTRITIONALE/100g</th></tr>
      <tr class="nutrition__gap"><td colspan="2"></td></tr>
      <tr><td>Energy</td><td>55.8g</td></tr>
      <tr><td>Fat</td><td>3.7g</td></tr>
      <tr><td>&nbsp;-Carbohydrate</td><td>14g</td></tr>
      <tr><td>Dietary Fiber</td><td>3.8g</td></tr>
      <tr><td>&nbsp;-Trans fat</td><td>21.7g</td></tr>
      <tr><td>Cholesterol</td><td>7g</td></tr>
      <tr><td>Protein</td><td>0g</td></tr>
    </table>

    <div class="net-weight">250g</div>

    <div class="distributor">
      Distribuitor: Orevia Trade SRL<br>
      Târgu Mureș, str. Livezii 14<br>
      Ambalat în Romania
    </div>
  </article>
</body>
</html>
```